Need a book cover design for a Lumora Book

Book has a long title and sub title so lots of words to fit on the cover.

I can be flexible a bit with the sub title due to the length of it but ideally i can get a design that takes everything.

Here is the title:

Tidal Geology: The Roots of Erosion, Sedimentation, and Canyon Forming

Sub Title/Heading
An Easy Primer on Coastal Cliffs, Dune Drift, River Beds, and Delta Mapping Methods

```html
<!DOCTYPE html>
<html lang="en">
<head>
<meta charset="utf-8">
<title>Tidal Geology — Book Cover</title>
<link rel="stylesheet" href="https://fonts.googleapis.com/css2?family=Oswald:wght@500;600;700&family=Montserrat:wght@300&display=swap">
<style>
  :root {
    --page-bg: #c9c9c9;
    --cover-navy: #06143a;
    --ink-white: #ffffff;
    --glow-bright: #3f8cff;
    --glow-mid: #1a4fc4;
    --glow-deep: #0b2470;
  }
  * { margin: 0; padding: 0; box-sizing: border-box; }
  html, body {
    width: 1200px;
    height: 1112px;
    overflow: hidden;
    background: var(--page-bg);
  }
  .cover {
    position: absolute;
    left: 240px;
    top: 56px;
    width: 720px;
    height: 1000px;
    background: var(--cover-navy);
    overflow: hidden;
    color: var(--ink-white);
  }
  .cover-art {
    position: absolute;
    left: 55px;
    top: 290px;
    width: 610px;
    height: 470px;
    border-radius: 50%;
    background: radial-gradient(ellipse at 50% 50%,
      var(--glow-bright) 0%,
      var(--glow-mid) 30%,
      var(--glow-deep) 58%,
      rgba(6, 20, 58, 0) 72%);
    opacity: 0.85;
  }
  .title {
    position: absolute;
    left: 107px;
    top: 128px;
    font-family: "Oswald", sans-serif;
    font-weight: 700;
    font-size: 124px;
    line-height: 118px;
    letter-spacing: -1px;
    text-transform: uppercase;
  }
  .topics {
    position: absolute;
    left: 107px;
    top: 404px;
    font-family: "Oswald", sans-serif;
    font-weight: 600;
    text-transform: uppercase;
    letter-spacing: -0.3px;
  }
  .topics span { display: block; line-height: 1.08; }
  .topics .t-1 { font-size: 31px; }
  .topics .t-2 { font-size: 34px; }
  .topics .t-3 { font-size: 30px; }
  .topics .t-4 { font-size: 28px; }
  .topics .t-5 { font-size: 36px; }
  .topics-rule {
    position: absolute;
    left: 108px;
    top: 624px;
    width: 166px;
    height: 3px;
    background: var(--ink-white);
  }
  .subtitle {
    position: absolute;
    left: 80px;
    width: 560px;
    top: 776px;
    text-align: center;
    font-family: "Oswald", sans-serif;
    font-weight: 500;
    font-size: 21px;
    line-height: 28px;
    letter-spacing: -0.2px;
  }
  .author {
    position: absolute;
    left: 0;
    width: 100%;
    top: 906px;
    text-align: center;
    font-family: "Montserrat", sans-serif;
    font-weight: 300;
    font-size: 24px;
    letter-spacing: 3px;
    text-transform: uppercase;
  }
</style>
</head>
<body>
  <main class="cover">
    <div class="cover-art" role="img" aria-label="Glowing blue particle wave field with concentric ripples"></div>

    <h1 class="title">Tidal<br>Geology</h1>

    <h2 class="topics">
      <span class="t-1">The Roots</span>
      <span class="t-2">of Erosion</span>
      <span class="t-3">Sedimentation</span>
      <span class="t-4">and</span>
      <span class="t-5">Canyon Forming</span>
    </h2>
    <div class="topics-rule"></div>

    <p class="subtitle">An Easy Primer on Coastal Cliffs, Dune Drift, River Beds,<br>and Delta Mapping Methods</p>

    <p class="author">John Doe</p>
  </main>
</body>
</html>
```